Harbor Crest One Page/2 Side Brochure

https://www.harborcrest-example.org/claims-recovery-program/
We need a revised professional design to replace the attached amateur design. HC does medical claim audits solely for hospitals to capture underpaid claims by insurers. All of the copy essentially needs to remain but we are open to design ideas. Obviously the RED FILL NEEDS TO GO and the copy in the two red fill areas should be flipped front to back. The red fill copy on the front tells 'how' we do it which should be on the back and the red fill copy on the back tells 'what' we do which should be on the front. We would like a clean look with a few pics depicting hospitals/financial savings (one attached)

```html
<!DOCTYPE html>
<html lang="en">
<head>
<meta charset="utf-8">
<title>Claims Recovery, Community Enrichment — Harbor Crest</title>
<link href="https://fonts.googleapis.com/css2?family=Playfair+Display:ital,wght@0,700;0,900;1,400&family=Roboto:wght@400;700&display=swap" rel="stylesheet">
<style>
  :root {
    --paper: #ffffff;
    --ink: #1c1c1c;
    --heading-grey: #7a7a7a;
    --money-light: #d9dcd6;
    --money-mid: #8d9590;
    --money-dark: #3f4a52;
    --accent-green: #3f9a2b;
    --numeral-ring: #d4d4d4;
    --numeral: #b5b5b5;
    --photo-a: #e7e8e3;
    --photo-b: #a9aea6;
    --photo-c: #6f7670;
  }
  * { margin: 0; padding: 0; box-sizing: border-box; }
  html, body { width: 1200px; height: 1000px; overflow: hidden; background: var(--paper); }
  .brochure { position: relative; width: 1200px; height: 1000px; color: var(--ink); font-family: "Roboto", Arial, sans-serif; }

  .headline { position: absolute; left: 272px; top: 34px; width: 440px; font-family: "Playfair Display", Georgia, serif; font-weight: 900; text-transform: uppercase; }
  .headline-money { display: block; font-size: 74px; line-height: 70px; letter-spacing: -1px; white-space: nowrap;
    transform: scaleY(1.1); transform-origin: left top;
    background: linear-gradient(160deg, var(--money-light) 0%, var(--money-mid) 35%, var(--money-dark) 55%, var(--money-mid) 75%, var(--money-light) 100%);
    -webkit-background-clip: text; background-clip: text; color: transparent;
    -webkit-text-stroke: 1px #6b716c; }
  .headline-money + .headline-money { margin-top: 0; }
  .headline-sub { display: block; font-size: 42px; line-height: 47px; color: var(--heading-grey); font-weight: 700; letter-spacing: 0.5px; white-space: nowrap; }
  .headline-money + .headline-sub { margin-top: 6px; }

  .hero-photo { position: absolute; left: 725px; top: 50px; width: 201px; height: 161px;
    background: radial-gradient(circle at 40% 45%, var(--photo-a) 0%, var(--photo-b) 45%, var(--photo-c) 100%); }

  .tagline { position: absolute; left: 275px; top: 290px; width: 670px; font-family: "Playfair Display", Georgia, serif; font-style: italic; font-size: 22px; line-height: 28px; }

  .intro { position: absolute; left: 275px; top: 366px; width: 405px; font-size: 14px; line-height: 18px; }
  .intro p + p { margin-top: 10px; }

  .steps { position: absolute; left: 274px; top: 518px; width: 420px; list-style: none; }
  .step { position: absolute; left: 0; width: 420px; display: flex; align-items: center; }
  .step-number { position: absolute; left: 0; width: 30px; height: 30px; border: 1.5px solid var(--numeral-ring); border-radius: 50%;
    display: flex; align-items: center; justify-content: center; font-family: "Playfair Display", Georgia, serif; font-style: italic; font-size: 18px; color: var(--numeral); }
  .step-text { margin-left: 52px; width: 366px; font-size: 12px; line-height: 15.3px; }

  .pitch { position: absolute; left: 725px; top: 362px; width: 206px; font-family: "Playfair Display", Georgia, serif; font-style: italic; font-size: 25px; line-height: 34.4px; color: var(--accent-green); }
  .pitch p + p { margin-top: 10px; }

  .signoff { position: absolute; left: 722px; top: 904px; width: 205px; height: 46px; }
  .brand { position: absolute; left: 0; top: 6px; display: flex; align-items: center; gap: 4px; font-family: "Roboto", Arial, sans-serif; font-weight: 700; font-size: 10px; line-height: 12px; color: var(--accent-green); }
  .brand-dot { width: 12px; height: 12px; border-radius: 50%; background: var(--accent-green); flex: none; }
  .contact { position: absolute; right: 0; top: 14px; width: 142px; text-align: center; font-family: Arial, "Roboto", sans-serif; font-weight: 700; font-size: 11px; line-height: 15px; }
</style>
</head>
<body>
<main class="brochure">
  <h1 class="headline">
    <span class="headline-money">Claims</span>
    <span class="headline-money">Recovery,</span>
    <span class="headline-sub">Community</span>
    <span class="headline-sub">Enrichment</span>
  </h1>

  <div class="hero-photo" role="img" aria-label="Photo of a silver stethoscope resting on a pile of hundred-dollar bills"></div>

  <p class="tagline">The ideal funding vehicle for your healthcare system to give back to the causes close to your heart!</p>

  <section class="intro">
    <p>An estimated $125B is lost by healthcare systems each year due to underpaid claims.</p>
    <p>With up-front costs waived, Harbor Crest’ Claims Recovery Program is the perfect way to easily and efficiently reclaim lost revenue for your healthcare system, while generating much-needed funds for your organization’s philanthropic endeavors! All in 6 easy steps…</p>
  </section>

  <ol class="steps">
    <li class="step" style="top:0;height:30px;"><span class="step-number">1</span><span class="step-text">$50,000 up-front cost WAIVED; there is zero risk.</span></li>
    <li class="step" style="top:56px;height:62px;"><span class="step-number">2</span><span class="step-text">Analysis of your organization’s $0-balance accounts going back 12 months. These are not billing code erros, collections, PHI, modifiers or denials – simply accounts which have been „closed according to contract.”</span></li>
    <li class="step" style="top:142px;height:46px;"><span class="step-number">3</span><span class="step-text">Your Crest Recovery Services Team ensures data collection, implementation and analysis are simple and efficient, with minimal time invested from your staff.</span></li>
    <li class="step" style="top:204px;height:62px;"><span class="step-number">4</span><span class="step-text">Timelines for data retrieval, implementation, analysis completion and recovery period are established throughout the program to you keep you apprised of action steps, milestones, criteria of success and final result.</span></li>
    <li class="step" style="top:282px;height:78px;"><span class="step-number">5</span><span class="step-text">Analysis and recovery are non-threatening to payors; relationship is always conducted with professionalism and respect. In fact, payors allocate money to reserves for these situations and are egar to make organizations whole in the event of uncovered underpayments.</span></li>
    <li class="step" style="top:378px;height:46px;"><span class="step-number">6</span><span class="step-text">In addition to funds recovered, the analysis provides valuable intelligence in terms of contract updates and management, as well as payor-payee relations.</span></li>
  </ol>

  <aside class="pitch">
    <p>Imagine all the lives that can be changed in your community by implementing this no-risk program in your organization today!</p>
    <p>Claims Recovery, Community Enrichment guarantees a way to fund wishes granted daily!</p>
  </aside>

  <footer class="signoff">
    <div class="brand"><span class="brand-dot"></span><span>Harbor<br>Crest</span></div>
    <div class="contact">855-555-0142<br>www.HarborCrest-example.org</div>
  </footer>
</main>
</body>
</html>
```